Valduro.com needs a Mobile FIRST Site

Valduro.com is an insurance broker based in Panama City, Panama that plans to sell car and motorcycle insurance online.

We need to design a total of 5 pages (two of those are A/B test pages). The site will be responsive and will be programmed in React. We will be using Brisk Widget´s library to code Valduro.com. Keep in mind that we are using Brisk Widget to program the site´s functions, not to create the "look and feel" of the site, that is obviously your job. You can learn more about Brisk Widget here... https://brisk-widget.example/

We have created wireframes for the app. Please follow and keep in mind the instructions in the wireframes. You can change things here and there as long as the core functions and goals stay intact. We have uploaded the wireframes along with the company logo and color.

We are planning to A/B test the site´s home page so we need to design two homepages. You can find homepage A and B in the wireframes provided.

We speak Spanish in Panama but you can design the site in English. We can change the text once we receive the designs.

Target Market(s)

25-45 year olds who own a car or motorcylcle and own a credit card.

Industry/Entity Type

Insurance

Font styles to use
Sans Serif

Requirements
Must have
• Follow the wireframes provided and the logo colors.
Nice to have
• Please look at the Image I´ve uploaded from DeskHaven, use it as reference to create HomePage A.

```html
<!DOCTYPE html>
<html lang="es">
<head>
<meta charset="utf-8">
<title>Valduro.com – Claim Aqui</title>
<link href="https://fonts.googleapis.com/css2?family=Open+Sans:wght@400;600;700&display=swap" rel="stylesheet">
<style>
  :root {
    --brand: #341f6e;
    --page-bg: #e6e6e6;
    --panel-bg: #d2d2d2;
    --tab-off: #b0b0b0;
    --ink: #222222;
    --ink-soft: #333333;
    --muted: #a9a9a9;
    --dark: #1e1e1e;
    --white: #ffffff;
    --track: #e8e8e8;
    --line: #cfcfcf;
  }
  * { box-sizing: border-box; margin: 0; padding: 0; }
  html, body { width: 1200px; height: 3041px; overflow: hidden; background: var(--page-bg); }
  body { font-family: "Open Sans", Arial, sans-serif; color: var(--ink); }
  .page {
    position: relative; width: 592px; height: 1500px;
    transform: scale(2.027027); transform-origin: 0 0;
    background: var(--page-bg);
  }
  .abs { position: absolute; }

  .site-header { left: 0; top: 0; width: 592px; height: 92px; background: var(--brand);
    display: flex; align-items: center; justify-content: center; }
  .brand-name { color: var(--white); font-weight: 700; font-size: 34px; letter-spacing: -0.5px; }

  .hero-title { left: 0; width: 592px; top: 126px; text-align: center; color: var(--brand);
    font-weight: 700; font-size: 48px; line-height: 64px; }
  .hero-text { left: 18px; width: 556px; top: 197px; text-align: center; color: var(--ink-soft);
    font-size: 16px; line-height: 28.5px; }

  .step { top: 308px; height: 92px; width: 167px; border-radius: 12px; background: var(--white);
    border: 1px solid var(--line); color: var(--muted); text-align: center;
    display: flex; flex-direction: column; justify-content: center; font-weight: 600; font-size: 24px; line-height: 32px; }
  .step--active { background: var(--dark); border-color: var(--dark); color: var(--white); }
  .step-number { font-weight: 700; }
  .step-link { top: 351px; height: 6px; width: 28px; }
  .step-link--done { left: 185px; background: var(--dark); }
  .step-link--todo { left: 379px; background: var(--muted); }

  .plans { left: 18px; top: 437px; width: 556px; height: 905px; background: var(--panel-bg); }
  .tab { top: 0; height: 91px; width: 278px; display: flex; align-items: center; justify-content: center;
    gap: 16px; color: var(--white); font-size: 38px; font-weight: 600; }
  .tab--cars { left: 0; background: var(--brand); }
  .tab--motos { left: 278px; background: var(--tab-off); }
  .tab-rule { left: 0; top: 91px; width: 556px; height: 8px; background: var(--brand); }

  .carousel-arrow { top: 487px; width: 14px; height: 24px; }

  .plan-card { top: 118px; width: 241px; height: 758px; background: var(--white); }
  .plan-card--a { left: 28px; }
  .plan-card--b { left: 287px; }
  .plan-photo { left: 10px; top: 9px; width: 222px; height: 167px; }
  .plan-photo--road { background: linear-gradient(160deg, #d8c8a8 0%, #8a6a52 40%, #9a1f26 65%, #3a3634 100%); }
  .plan-photo--studio { background: linear-gradient(180deg, #5f7f88 0%, #8aa4aa 45%, #b2242c 70%, #2c2f33 100%); }
  .featured-badge { right: 10px; top: 9px; width: 31px; height: 31px; background: var(--white);
    display: flex; align-items: center; justify-content: center; }
  .plan-price { left: 0; width: 241px; top: 181px; text-align: center; color: var(--brand);
    font-weight: 700; font-size: 36px; line-height: 50px; }
  .metric-label { left: 10px; font-size: 13px; line-height: 18px; color: var(--ink); }
  .metric-bar { left: 13px; width: 222px; height: 37px; background: var(--track); }
  .metric-fill { position: absolute; left: 0; top: 0; height: 37px; width: 157px; background: var(--brand);
    color: var(--white); font-weight: 700; font-size: 16px; line-height: 37px; padding-left: 12px; }
  .plan-divider { left: 0; top: 515px; width: 241px; height: 1px; background: var(--line); }
  .benefits-title { left: 10px; top: 539px; font-size: 22px; line-height: 32px; color: var(--ink); }
  .benefits-list { left: 12px; top: 576px; list-style: none; font-size: 15px; line-height: 29.5px; color: var(--ink-soft); }
  .benefits-list li::before { content: "•"; margin-right: 8px; font-size: 12px; }
  .buy-button { left: 10px; top: 687px; width: 222px; height: 55px; border-radius: 12px; background: var(--brand);
    color: var(--white); font-weight: 700; font-size: 24px; display: flex; align-items: center; justify-content: center; }

  .copyright { left: 0; width: 592px; top: 1373px; text-align: center; font-size: 16px; color: var(--ink-soft); word-spacing: 3px; }
  .social-dot { top: 1414px; width: 56px; height: 56px; border-radius: 50%; background: var(--ink-soft); }
  .page-tag { left: 552px; top: 1468px; font-size: 15px; color: var(--ink); }
</style>
</head>
<body>
<div class="page">
  <header class="site-header abs"><span class="brand-name">Valduro.com</span></header>

  <h1 class="hero-title abs">Claim Aqui</h1>
  <p class="hero-text abs">Nullam lorem urna, tempus eget mollis et, dapibus ac sem. Sus pendis-se gravida ornare erat sed pulvinar. Vestibulum luctus ex in egestas fringilla. Fusce nec leo ac urna pulvinar auctor.</p>

  <div class="step step--active abs" style="left:18px"><span class="step-number">1</span><span>Elige</span></div>
  <div class="step-link step-link--done abs"></div>
  <div class="step abs" style="left:213px"><span class="step-number">2</span><span>Datos</span></div>
  <div class="step-link step-link--todo abs"></div>
  <div class="step abs" style="left:407px"><span class="step-number">3</span><span>Paga</span></div>

  <section class="plans abs">
    <div class="tab tab--cars abs">
      <svg width="64" height="46" viewBox="0 0 64 46" aria-hidden="true">
        <path fill="#fff" d="M12 4 Q14 0 20 0 H44 Q50 0 52 4 L58 16 Q64 18 64 24 V38 H56 V44 H46 V38 H18 V44 H8 V38 H0 V24 Q0 18 6 16 Z"/>
        <path fill="#341f6e" d="M14 16 L18 7 H46 L50 16 Z"/>
        <circle cx="12" cy="26" r="5" fill="#341f6e"/><circle cx="52" cy="26" r="5" fill="#341f6e"/>
        <rect x="22" y="24" width="20" height="5" fill="#341f6e"/>
      </svg>
      <span>Carros</span>
    </div>
    <div class="tab tab--motos abs">
      <svg width="76" height="48" viewBox="0 0 76 48" aria-hidden="true">
        <circle cx="14" cy="34" r="11" fill="none" stroke="#fff" stroke-width="6"/>
        <circle cx="62" cy="34" r="11" fill="none" stroke="#fff" stroke-width="6"/>
        <path fill="#fff" d="M8 22 L22 14 H34 L42 22 L50 10 H58 L66 24 L60 26 L54 18 L46 32 H24 Z"/>
        <rect x="46" y="2" width="12" height="6" fill="#fff"/>
      </svg>
      <span>Motos</span>
    </div>
    <div class="tab-rule abs"></div>

    <svg class="carousel-arrow abs" style="left:7px" viewBox="0 0 14 24" aria-hidden="true"><path d="M12 2 L3 12 L12 22" fill="none" stroke="#555" stroke-width="3"/></svg>
    <svg class="carousel-arrow abs" style="left:535px" viewBox="0 0 14 24" aria-hidden="true"><path d="M2 2 L11 12 L2 22" fill="none" stroke="#555" stroke-width="3"/></svg>

    <article class="plan-card plan-card--a abs">
      <div class="plan-photo plan-photo--road abs" role="img" aria-label="Red sports car driving on a road"></div>
      <div class="featured-badge abs">
        <svg width="18" height="18" viewBox="0 0 24 24" aria-hidden="true"><path fill="#341f6e" d="M12 1 L15 9 H23 L16.5 14 L19 22 L12 17 L5 22 L7.5 14 L1 9 H9 Z"/></svg>
      </div>
      <div class="plan-price abs">$150.00</div>
      <div class="metric-label abs" style="top:253px">Insurance Coverage :</div>
      <div class="metric-bar abs" style="top:274px;left:13px;width:222px"><div class="metric-fill">$10,000</div></div>
      <div class="metric-label abs" style="top:336px">Coverage Limit :</div>
      <div class="metric-bar abs" style="top:357px;width:219px"><div class="metric-fill">$15,000</div></div>
      <div class="metric-label abs" style="top:420px">Nulla tristique :</div>
      <div class="metric-bar abs" style="top:441px;left:10px"><div class="metric-fill">$12,000</div></div>
      <div class="plan-divider abs"></div>
      <h2 class="benefits-title abs">Beneficios</h2>
      <ul class="benefits-list abs">
        <li>Aliquam erat volutpat</li>
        <li>Etiam quis aliquet risus</li>
        <li>Duis ornare erat eget</li>
      </ul>
      <div class="buy-button abs">COMPRAR</div>
    </article>

    <article class="plan-card plan-card--b abs">
      <div class="plan-photo plan-photo--studio abs" role="img" aria-label="Red sedan parked in a studio with reflective floor"></div>
      <div class="plan-price abs">$150.00</div>
      <div class="metric-label abs" style="top:253px">Insurance Coverage :</div>
      <div class="metric-bar abs" style="top:274px"><div class="metric-fill">$11,000</div></div>
      <div class="metric-label abs" style="top:336px">Coverage Limit :</div>
      <div class="metric-bar abs" style="top:357px;width:218px"><div class="metric-fill">$18,000</div></div>
      <div class="plan-divider abs"></div>
      <h2 class="benefits-title abs">Beneficios</h2>
      <ul class="benefits-list abs">
        <li>Nam tempus, bibendum</li>
        <li>Aliquam erat volutpat</li>
      </ul>
      <div class="buy-button abs">COMPRAR</div>
    </article>
  </section>

  <footer>
    <p class="copyright abs">Copyright &nbsp;©&nbsp; 2018 &nbsp;Valduro. &nbsp;All rights reserved.</p>
    <span class="social-dot abs" style="left:157px" aria-label="Social link"></span>
    <span class="social-dot abs" style="left:231px" aria-label="Social link"></span>
    <span class="social-dot abs" style="left:305px" aria-label="Social link"></span>
    <span class="social-dot abs" style="left:379px" aria-label="Social link"></span>
  </footer>
  <span class="page-tag abs">M2</span>
</div>
</body>
</html>
```